The Open Compass Field Journeys Travel Brochure

I'm looking for a brochure design for a new travel product - The Open Compass Field Journeys, catering for students above 12 years old. Target audience are schools that do destination projects. Brochure to be read by head teacher, parents and students.

Brochure should be A4 in size, 4-6 pages. Format of brochure is hard cover (a folder) with inlet for flyers. Flyers for destinations will be updated from time to time.

Finished job needs to be converted to electronic format for website and email proposal usage.

Attached is text to be used on brochure. Order of section can be adjusted.

For "Elements of the trip", please understand the contents and explain/display it in a graphic form.

For flyer, please come out with a template that I can use for other destinations. The main elements - what's included, number of days, location for pictures, itinerary, educational focus, should be alterable. Attached are text for two sample destinations.
Also attached (tour itinerary example) a version of flyer that I like.

I'm attaching some pictures here. If you find more suitable pictures, please feel free to use them.

Reason: I'm extending the deadline of this project by 4 days, as I need to add details & photo of another travel specialist in personnel session (total of 3 members). Also, in view of the amount of work a designer has to do for this project, I'm giving you more time for submission. Please do not hesitate to be in touch should you need more than 4 days extension. Thank you.

Target Market(s)

Schools - especially the head teacher and parents, to send students above 12 years old to travel

Industry/Entity Type

Electronic

Requirements
Must have
• This is a travel brochure with education elements in it. Parents feel better when their children are travelling for a purpose and lead by responsible teachers/adults whom they can trust. So, the design has to emphasis that education elements and safety are our utmost priority.
Nice to have
• We specialise in environmental study. So, it is nice to have the environmental touch in the design.
Should not have
• Our target market segment is the Middle East, which can be quite sensitive to religion. I prefer not to have any religious related illustration on the design.

```html
<!DOCTYPE html>
<html lang="en">
<head>
<meta charset="utf-8">
<title>Greece – 7 Day Journey Flyer | The Open Compass Field Journeys</title>
<link rel="stylesheet" href="https://fonts.googleapis.com/css2?family=Exo+2:ital,wght@0,600;1,500;1,600;1,700&family=Open+Sans:wght@400;700&display=swap">
<style>
  :root {
    --blue: #0a86cf;
    --blue-deep: #0066b3;
    --blue-light: #4fb3ec;
    --text-grey: #666666;
    --heading-blue: #1a8fd6;
    --paper: #ffffff;
    --gutter: #f0f0f0;
  }
  * { margin: 0; padding: 0; box-sizing: border-box; }
  html, body { width: 1200px; height: 858px; overflow: hidden; background: var(--paper); }
  body { font-family: "Open Sans", Arial, sans-serif; color: var(--text-grey); position: relative; }

  .spread { position: relative; width: 1200px; height: 858px; }
  .page { position: absolute; top: 0; height: 858px; overflow: hidden; }
  .page--cover { left: 0; width: 596px; }
  .page--inside { left: 600px; width: 600px; }
  .page-gutter { position: absolute; left: 596px; top: 0; width: 4px; height: 858px; background: var(--gutter); }

  .cover-photo {
    position: absolute; left: 0; top: 170px; width: 596px; height: 688px;
    background:
      radial-gradient(ellipse 260px 200px at 270px 470px, rgba(178,98,62,.85) 0%, rgba(178,98,62,0) 70%),
      radial-gradient(ellipse 200px 260px at 110px 560px, rgba(58,66,40,.8) 0%, rgba(58,66,40,0) 75%),
      radial-gradient(ellipse 220px 220px at 430px 540px, rgba(52,62,38,.75) 0%, rgba(52,62,38,0) 75%),
      linear-gradient(180deg, #8797ab 0%, #a9b4c2 22%, #c9ccce 38%, #b89a74 55%, #8c7656 70%, #5a5a42 85%, #4a4a3c 100%);
  }
  .cover-art { position: absolute; inset: 0; }

  .brand { position: absolute; display: flex; align-items: center; gap: 8px;
           font-family: "Exo 2", Arial, sans-serif; font-weight: 600; color: var(--blue-deep); font-size: 17px; }
  .brand__mark { width: 12px; height: 12px; background: var(--blue-deep); }
  .page--cover .brand { left: 66px; top: 104px; }
  .page--inside .brand { left: 46px; top: 128px; }

  .cover-title { position: absolute; right: 40px; top: 694px; text-align: right; color: #fff; }
  .cover-title h1 { font-family: "Open Sans", Arial, sans-serif; font-weight: 700; font-size: 66px; line-height: 1;
                    letter-spacing: -0.5px; text-shadow: 2px 3px 4px rgba(0,0,0,.55); }
  .cover-title p { font-family: "Exo 2", Arial, sans-serif; font-style: italic; font-weight: 600; font-size: 19px; margin-top: 14px;
                   text-shadow: 1px 1px 3px rgba(0,0,0,.55); }

  .focus { position: absolute; left: 206px; top: 64px; font-size: 14.5px; line-height: 22px; }
  .focus dt { display: inline; color: var(--heading-blue); font-weight: 700; }
  .focus dd { display: inline; }
  .focus .row { display: block; }

  .trip-heading { position: absolute; left: 27px; top: 192px; font-family: "Exo 2", Arial, sans-serif;
                  font-style: italic; font-weight: 700; color: var(--heading-blue); }
  .trip-heading .dest { display: block; font-size: 36px; line-height: 44px; }
  .trip-heading .sub { display: block; font-size: 28px; line-height: 36px; }

  .itinerary { position: absolute; left: 34px; top: 294px; list-style: none; }
  .itinerary li { height: 24px; display: flex; align-items: baseline; }
  .itinerary .day { width: 34px; color: var(--heading-blue); font-size: 10.5px; }
  .itinerary .stop { font-family: "Exo 2", Arial, sans-serif; font-style: italic; font-weight: 500; font-size: 13.5px; color: var(--text-grey); }

  .photo { position: absolute; box-shadow: 3px 4px 8px rgba(0,0,0,.4); }
  .photo--temple { left: 342px; top: 183px; width: 170px; height: 132px;
    background:
      radial-gradient(ellipse 110px 80px at 120px 90px, rgba(196,178,146,.95) 0%, rgba(196,178,146,0) 75%),
      radial-gradient(ellipse 70px 60px at 95px 40px, rgba(92,84,72,.7) 0%, rgba(92,84,72,0) 80%),
      linear-gradient(160deg, #9dbde0 0%, #c3d4e6 30%, #8d8574 60%, #6b6357 100%); }
  .photo--columns { left: 50px; top: 478px; width: 145px; height: 217px;
    background:
      radial-gradient(ellipse 60px 120px at 80px 130px, rgba(201,186,160,.9) 0%, rgba(201,186,160,0) 80%),
      linear-gradient(180deg, #b6cde4 0%, #8f8676 18%, #b8a98e 45%, #8d8070 75%, #6e6456 100%); }
  .photo--arch { left: 230px; top: 453px; width: 273px; height: 183px;
    background:
      radial-gradient(ellipse 150px 50px at 136px 160px, rgba(110,100,86,.9) 0%, rgba(110,100,86,0) 80%),
      radial-gradient(ellipse 140px 40px at 136px 50px, rgba(120,108,92,.75) 0%, rgba(120,108,92,0) 80%),
      linear-gradient(180deg, #5f8fcf 0%, #8fb2e0 35%, #a9c4e6 55%, #8c8272 80%, #6a6152 100%); }

  .included { position: absolute; left: 273px; top: 656px; }
  .included h2 { font-size: 14px; font-weight: 700; color: var(--heading-blue); margin-bottom: 2px; }
  .included ul { list-style: none; font-size: 12.5px; line-height: 15.6px; color: var(--text-grey); }

  .corner-swoosh { position: absolute; left: 24px; top: 712px; }
</style>
</head>
<body>
<main class="spread">

  <section class="page page--cover">
    <div class="cover-photo" role="img" aria-label="Photograph of a domed stone building with terracotta roofs and tall cypress trees under a grey sky"></div>
    <svg class="cover-art" width="596" height="858" viewBox="0 0 596 858" aria-hidden="true">
      <defs>
        <linearGradient id="bandBlue" x1="0" y1="0" x2="1" y2="1">
          <stop offset="0" stop-color="#0a86cf"/>
          <stop offset="1" stop-color="#1196de"/>
        </linearGradient>
      </defs>
      <path d="M0 170 H360 C300 250 170 335 0 378 Z" fill="url(#bandBlue)"/>
      <path d="M0 378 C170 335 300 250 360 170 C290 260 170 345 0 400 Z" fill="#4fb3ec" opacity="0.9"/>
      <path d="M360 170 C420 110 500 60 596 28 V170 Z" fill="var(--blue)"/>
      <path d="M0 0 H596 V28 C500 60 420 110 360 170 H0 Z" fill="#ffffff"/>
      <path d="M360 170 C420 110 500 60 596 28" stroke="#d6ecf9" stroke-width="6" fill="none"/>
      <path d="M60 858 C250 850 460 760 596 640 V858 Z" fill="#555" opacity="0.55"/>
    </svg>
    <div class="brand"><span class="brand__mark"></span>Open Compass</div>
    <div class="cover-title">
      <h1>Greece</h1>
      <p>7 Day Journey through Greece</p>
    </div>
  </section>

  <div class="page-gutter"></div>

  <section class="page page--inside">
    <div class="brand"><span class="brand__mark"></span>Open Compass</div>

    <dl class="focus">
      <span class="row"><dt>Main focus subject:</dt> <dd>Geography</dd></span>
      <span class="row"><dt>Related subjects:</dt> <dd>&nbsp;History, Anthropology,</dd></span>
      <span class="row"><dd>Environmental Management, Art and Design</dd></span>
      <span class="row"><dt>Environmental focus:</dt> <dd>Marine ecology and</dd></span>
      <span class="row"><dd>related human threats</dd></span>
    </dl>

    <h2 class="trip-heading"><span class="dest">Greece</span><span class="sub">Itinerary</span></h2>

    <div class="photo photo--temple" role="img" aria-label="Photograph of a classical Greek temple with Doric columns"></div>

    <ol class="itinerary">
      <li><span class="day">Day 1</span><span class="stop">Arrival at Athens – Athens city tour</span></li>
      <li><span class="day">Day 2</span><span class="stop">Athens to Mykonos on cruise – Mykonos tour</span></li>
      <li><span class="day">Day 3</span><span class="stop">Mykonos to Kusadasi (Turkey) on cruise – Kusadasi tour</span></li>
      <li><span class="day">Day 4</span><span class="stop">Kusadasi to Santorini on cruise – Santorini and volcano tour</span></li>
      <li><span class="day">Day 5</span><span class="stop">Santorini to Athens on cruise – Athens second city tour</span></li>
      <li><span class="day">Day 6</span><span class="stop">Athens to Delphi by coach (2 hours) – visit hill towns on way – Delphi tour</span></li>
      <li><span class="day">Day 7</span><span class="stop">Departure</span></li>
    </ol>

    <div class="photo photo--columns" role="img" aria-label="Photograph of ancient marble columns seen from below"></div>
    <div class="photo photo--arch" role="img" aria-label="Photograph of an ancient stone gateway against a blue sky"></div>

    <div class="included">
      <h2>What's included in price:</h2>
      <ul>
        <li>Air ticket</li>
        <li>All accommodation</li>
        <li>Full time tour director</li>
        <li>Meals</li>
        <li>Tours led by local expert tour guides</li>
        <li>Entrance fees to attractions</li>
      </ul>
    </div>

    <svg class="corner-swoosh" width="145" height="105" viewBox="0 0 145 105" aria-hidden="true">
      <path d="M144 0 V70 H25 C60 35 100 12 144 0 Z" fill="var(--blue)"/>
      <path d="M0 72 H80 C55 85 30 96 0 104 Z" fill="var(--blue)"/>
    </svg>
  </section>

</main>
</body>
</html>
```